Affiche pour le concert d'un orchestre symphonique universitaire parisien
Bonjour,
Nos souhaitons recevoir des propositions d'affiches pour un concert que notre orchestre symphoniqe ainsi que son choeur (Ensemble et Chorale Estudiantine de Varenne) organise à l'occasion de ses 25 ans à l'auditorium de Onde Lumière
Description de l'entreprise
Nous sommes une association
La cible
Tout public interessé par la musique symphonique.
Couleurs, favoris et autres exigences:
Nous souhaitons pouvoir préciser les éléments d'information suivants sur l'affiche:
9ème symphonie de Valdmeyer
Palais des Ondes - Auditorium
Lundi 28 mai 2018 à 20 h 00
25ème anniversaire de l'Ensemble et Chorale des Facultés de Varenne
Sous le patronage de ...
Direction musicale :
Chef de choeur :
Soprano :
Alto :
Ténor :
Basse :
Présentation :
300x300

```html
<!DOCTYPE html>
<html lang="fr">
<head>
<meta charset="utf-8">
<title>9ème Symphonie de Valdmeyer – Palais des Ondes</title>
<link href="https://fonts.googleapis.com/css2?family=Bodoni+Moda:wght@500;600&family=Libre+Baskerville:ital,wght@0,400;1,400&family=Open+Sans:wght@400;700&display=swap" rel="stylesheet">
<style>
  :root {
    --ink: #1b1b1f;
    --night: #0c0c0d;
    --orange: #d8622a;
    --paper: #ffffff;
    --rule: #3a3a3a;
  }
  html, body { margin: 0; padding: 0; overflow: hidden; background: var(--paper); }
  .poster {
    position: relative; width: 849px; height: 1200px; overflow: hidden;
    background: var(--paper); color: var(--ink);
    font-family: "Libre Baskerville", Georgia, serif;
  }
  .night-band { position: absolute; left: 545px; top: 0; width: 304px; height: 1200px; background: var(--night); }
  .instrument-column {
    position: absolute; left: 430px; top: 0; width: 120px; height: 1200px;
    background: linear-gradient(90deg, rgba(12,12,13,0) 0%, rgba(12,12,13,.2) 50%, var(--night) 100%);
  }
  .orchestra-photo {
    position: absolute; left: 566px; top: 552px; width: 283px; height: 648px;
    background: radial-gradient(ellipse at 40% 30%, #8a4a2a 0%, #3d2218 40%, #141010 80%);
  }
  .anniversary {
    position: absolute; left: 488px; top: 68px; width: 347px; height: 90px;
    background: var(--orange); color: var(--paper);
    font-family: "Open Sans", Arial, sans-serif; box-sizing: border-box;
    padding: 10px 0 0 26px; line-height: 1.2;
  }
  .anniversary .lead { font-weight: 700; font-size: 20px; }
  .anniversary .lead sup { font-size: 12px; }
  .anniversary .org { font-size: 17px; text-transform: uppercase; letter-spacing: .3px; }

  .title { position: absolute; left: 52px; top: 385px; width: 440px; height: 130px; }
  .title .numeral {
    position: absolute; left: 0; top: -6px; font-family: "Bodoni Moda", serif;
    font-weight: 600; font-size: 148px; line-height: 1; color: var(--orange);
  }
  .title .ordinal {
    position: absolute; left: 106px; top: 6px; font-family: "Bodoni Moda", serif;
    font-size: 30px; line-height: 1; color: var(--orange);
  }
  .title .rule-top { position: absolute; left: 106px; top: 40px; width: 323px; border-top: 1.5px solid var(--rule); }
  .title .work { position: absolute; left: 104px; top: 42px; font-size: 38px; line-height: 1; letter-spacing: .3px; }
  .title .composer { position: absolute; left: 106px; top: 88px; font-size: 28px; line-height: 1; letter-spacing: .3px; }
  .title .rule-bottom { position: absolute; left: 106px; top: 122px; width: 323px; border-top: 1.5px solid var(--rule); }

  .venue {
    position: absolute; left: 64px; top: 590px; width: 426px; text-align: center;
    font-size: 16px; letter-spacing: 2.5px; text-transform: uppercase;
  }
  .date {
    position: absolute; left: 64px; top: 630px; width: 426px; text-align: center;
    font-style: italic; font-size: 34px; color: var(--orange);
  }
  .date-rule { position: absolute; left: 96px; top: 684px; width: 385px; height: 14px; }
  .time {
    position: absolute; left: 350px; top: 700px; width: 128px; text-align: right;
    font-style: italic; font-size: 21px; color: var(--orange);
  }
  .credits {
    position: absolute; left: 57px; top: 968px; font-style: italic; font-size: 13px;
    line-height: 20px; margin: 0; padding: 0; list-style: none;
  }
  .credits li.gap { margin-top: 18px; }
</style>
</head>
<body>
<main class="poster">
  <div class="instrument-column" role="img" aria-label="Colonne de silhouettes d'instruments et de notes de musique : clavier, notes, clé de fa, guitare, clé de sol, saxophone, tambourin"></div>
  <div class="night-band"></div>
  <div class="orchestra-photo" role="img" aria-label="Photographie floue de violonistes d'un orchestre en concert"></div>

  <div class="anniversary">
    <div class="lead">25<sup>ÈME</sup> ANNIVERSAIRE</div>
    <div class="org">de l'Ensemble et Chorale</div>
    <div class="org">des Facultés de Varenne</div>
  </div>

  <div class="title">
    <span class="numeral">9</span>
    <span class="ordinal">ème</span>
    <span class="rule-top"></span>
    <span class="work">SYMPHONIE</span>
    <span class="composer">DE VALDMEYER</span>
    <span class="rule-bottom"></span>
  </div>

  <div class="venue">Palais des Ondes - Auditorium</div>
  <div class="date">lundi 28 mai 2018</div>
  <svg class="date-rule" viewBox="0 0 385 14" aria-hidden="true">
    <line x1="0" y1="7" x2="385" y2="7" stroke="#3a3a3a" stroke-width="1.5"/>
  </svg>
  <div class="time">à 20h00</div>

  <ul class="credits">
    <li>Sous le patronage de Nom Prénom</li>
    <li>Direction musicale : Nom Prénom</li>
    <li>Chef de choeur : Nom Prénom</li>
    <li class="gap">Soprano : Nom Prénom</li>
    <li>Alto : Nom Prénom</li>
    <li>Ténor : Nom Prénom</li>
    <li>Basse : Nom Prénom</li>
    <li>Présentation : Nom Prénom</li>
  </ul>
</main>
</body>
</html>
```